Dalton Power Supply, Inc. Business Card Design

We are an Electrical Distributor looking for a Modern, Professional Business Card design.

Target Market(s)

Residential Commercial Industrial

Industry/Entity Type

Electrical

Contact Information for Business Card

Dalton Power Supply, Inc.
418 Maple Ridge Lane
Brookvale, NC 27514
555-214-7630
555-214-8842 Fax
daltonpower@brightmail-example.net

```html
<!DOCTYPE html>
<html lang="en">
<head>
<meta charset="utf-8">
<title>Dalton Power Supply, Inc. – Business Card</title>
<link rel="stylesheet" href="https://fonts.googleapis.com/css2?family=Exo+2:wght@400;600;700&display=swap">
<style>
  :root {
    --stage: #e9e7e4;
    --card: #fdfdfd;
    --brand-blue: #2f86d0;
    --text-grey: #6b6d70;
    --facet-light: #dbe8f3;
    --facet-mid: #b9d3ea;
    --facet-grey: #d6d9dd;
  }
  * { box-sizing: border-box; margin: 0; padding: 0; }
  html, body {
    width: 1200px;
    height: 675px;
    overflow: hidden;
    background: var(--stage);
    font-family: "Exo 2", sans-serif;
  }
  .stage {
    width: 1200px;
    height: 675px;
    display: flex;
    align-items: center;
    justify-content: center;
  }
  .business-card {
    position: relative;
    width: 700px;
    height: 400px;
    background: var(--card);
    border-radius: 6px;
    box-shadow: 0 12px 34px rgba(0, 0, 0, 0.12);
    overflow: hidden;
  }
  .brand {
    position: absolute;
    top: 70px;
    right: 60px;
    display: flex;
    align-items: center;
    gap: 14px;
  }
  .brand-mark {
    width: 34px;
    height: 34px;
    background: var(--brand-blue);
  }
  .brand-name {
    font-weight: 600;
    font-size: 30px;
    color: var(--brand-blue);
    letter-spacing: 0.5px;
  }
  .facets {
    position: absolute;
    right: 0;
    bottom: 0;
    width: 300px;
    height: 190px;
    background: linear-gradient(135deg, rgba(255,255,255,0) 0%, var(--facet-grey) 40%, var(--facet-light) 65%, var(--facet-mid) 100%);
    clip-path: polygon(30% 100%, 55% 20%, 100% 0, 100% 100%);
  }
  .person {
    position: absolute;
    left: 60px;
    top: 200px;
    color: var(--text-grey);
    font-size: 15px;
    line-height: 1.55;
  }
  .person-name {
    font-weight: 700;
    font-size: 19px;
    color: var(--brand-blue);
    letter-spacing: 1.5px;
    text-transform: uppercase;
    margin-bottom: 2px;
  }
  .person-title { margin-bottom: 10px; }
  .contact-list {
    position: absolute;
    left: 300px;
    top: 232px;
    list-style: none;
    color: var(--text-grey);
    font-size: 15px;
    line-height: 1.55;
  }
  .contact-item {
    display: flex;
    align-items: center;
    gap: 9px;
    margin-bottom: 3px;
  }
  .contact-icon {
    width: 15px;
    height: 15px;
    fill: var(--brand-blue);
    flex: none;
  }
</style>
</head>
<body>
<main class="stage">
  <article class="business-card">
    <div class="brand">
      <span class="brand-mark"></span>
      <span class="brand-name">Dalton Power Supply, Inc.</span>
    </div>

    <div class="facets" role="img" aria-label="Faceted light blue and grey angular decoration"></div>

    <section class="person">
      <p class="person-name">Evan Carter</p>
      <p class="person-title">Director</p>
      <p class="address-line">418 Maple Ridge Lane</p>
      <p class="address-line">Brookvale, NC 27514</p>
    </section>

    <ul class="contact-list">
      <li class="contact-item">
        <svg class="contact-icon" viewBox="0 0 16 16" aria-hidden="true"><path d="M3.6 1.2l2.2 2.6c.3.4.3.9 0 1.3L4.7 6.3c.9 2 2.6 3.7 4.9 4.9l1.2-1.1c.4-.3.9-.3 1.3 0l2.6 2.2c.4.3.4.9.1 1.3l-1.2 1.3c-.6.6-1.5.8-2.3.5C6.4 13.8 2.2 9.6.6 4.7.3 3.9.5 3 1.1 2.4L2.3 1.2c.4-.4 1-.3 1.3 0z"/></svg>
        <span>555-214-7630</span>
      </li>
      <li class="contact-item">
        <svg class="contact-icon" viewBox="0 0 16 16" aria-hidden="true"><path d="M4 1h8v4H4zM1 6h14v6h-2v3H3v-3H1zM4.5 10v3.5h7V10z"/></svg>
        <span>555-214-8842</span>
      </li>
      <li class="contact-item">
        <svg class="contact-icon" viewBox="0 0 16 16" aria-hidden="true"><path d="M1 3h14v10H1zM2.2 4.2v.4L8 8.6l5.8-4V4.2zM2.2 6v5.8h11.6V6L8 10z"/></svg>
        <span>daltonpower@brightmail-example.net</span>
      </li>
    </ul>
  </article>
</main>
</body>
</html>
```